Creative Businesss Card desgin!

Create a business card for our business Glint window cleaning!
We are open to creative ideas as long as it maintains a professional image.

Target Market(s)

Small Commercial window cleaning clients including car dealerships, strata manager, cafe

Industry/Entity Type

Window Cleaning

Contact Information for Business Card

Darren Pilkey
General Manager
Glint Window Cleaning

darren@glintservices.com.au
pane-tidy-corner.com.au
Ph: 1800 GO GLINT
Mob: 0438 572 619

Colors
fbed22
0392cd

Requirements
Should not have
• Stock window cleaning/ squeegee graphics

```html
<!DOCTYPE html>
<html lang="en">
<head>
<meta charset="utf-8">
<title>Glint Window Cleaning – Business Card</title>
<link href="https://fonts.googleapis.com/css2?family=Archivo:wght@400;800&display=swap" rel="stylesheet">
<style>
  :root {
    --brand-yellow: #e3d42a;
    --brand-blue: #0392cd;
    --card-mid: #0a7eab;
    --card-deep: #064a7a;
    --divider-lilac: #b7b3d6;
    --text-white: #ffffff;
    --backdrop: #1c1c1e;
  }
  * { margin: 0; padding: 0; box-sizing: border-box; }
  html, body {
    width: 1200px;
    height: 900px;
    overflow: hidden;
    background: var(--backdrop);
    font-family: "Archivo", "Helvetica Neue", Arial, sans-serif;
  }
  .canvas {
    position: relative;
    width: 1200px;
    height: 900px;
    display: flex;
    align-items: center;
    justify-content: center;
  }
  .business-card {
    position: relative;
    width: 1000px;
    height: 580px;
    background: radial-gradient(ellipse at 55% 55%, var(--card-mid) 0%, #08679a 55%, var(--card-deep) 100%);
    box-shadow: 0 20px 50px rgba(0,0,0,0.55);
  }
  .brand {
    position: absolute;
    left: 90px;
    top: 250px;
    display: flex;
    align-items: center;
    gap: 18px;
  }
  .brand-mark {
    width: 30px;
    height: 30px;
    background: var(--brand-yellow);
    flex: none;
  }
  .brand-name {
    color: var(--brand-yellow);
    font-weight: 800;
    font-size: 36px;
    line-height: 1.15;
    letter-spacing: 1px;
    text-transform: uppercase;
  }
  .brand-name span { display: block; }
  .divider {
    position: absolute;
    left: 540px;
    width: 2px;
  }
  .divider--name { top: 190px; height: 60px; background: var(--brand-yellow); }
  .divider--contact { top: 280px; height: 125px; background: var(--divider-lilac); }
  .person {
    position: absolute;
    left: 575px;
    top: 192px;
  }
  .person-name {
    color: var(--brand-yellow);
    font-weight: 800;
    font-size: 30px;
    letter-spacing: 1px;
    text-transform: uppercase;
  }
  .person-role {
    color: var(--text-white);
    font-weight: 400;
    font-size: 21px;
    margin-top: 2px;
  }
  .contact-list {
    position: absolute;
    left: 575px;
    top: 283px;
    list-style: none;
  }
  .contact-item {
    display: flex;
    align-items: center;
    gap: 12px;
    color: var(--text-white);
    font-size: 21px;
    line-height: 31px;
  }
  .contact-icon {
    width: 17px;
    height: 17px;
    flex: none;
  }
</style>
</head>
<body>
<main class="canvas">
  <section class="business-card">
    <div class="brand">
      <span class="brand-mark" aria-hidden="true"></span>
      <h1 class="brand-name"><span>Glint</span><span>Window Cleaning</span></h1>
    </div>

    <span class="divider divider--name"></span>
    <span class="divider divider--contact"></span>

    <div class="person">
      <p class="person-name">Darren Pilkey</p>
      <p class="person-role">General Manager</p>
    </div>

    <ul class="contact-list">
      <li class="contact-item">
        <svg class="contact-icon" viewBox="0 0 20 20" aria-hidden="true">
          <path d="M4 2 L8 2 L9 6 L7 8 Q9 12 12 13 L14 11 L18 12 L18 16 Q17 18 14 18 Q3 16 2 5 Q2 2 4 2 Z" fill="var(--brand-yellow)"/>
        </svg>
        <span>1800 GO GLINT</span>
      </li>
      <li class="contact-item">
        <svg class="contact-icon" viewBox="0 0 20 20" aria-hidden="true">
          <rect x="5" y="1.5" width="10" height="17" rx="1.5" fill="none" stroke="var(--brand-yellow)" stroke-width="1.8"/>
          <line x1="8.5" y1="15.5" x2="11.5" y2="15.5" stroke="var(--brand-yellow)" stroke-width="1.5"/>
        </svg>
        <span>0438 572 619</span>
      </li>
      <li class="contact-item">
        <svg class="contact-icon" viewBox="0 0 20 20" aria-hidden="true">
          <rect x="1.5" y="4" width="17" height="12" fill="none" stroke="var(--brand-yellow)" stroke-width="1.6"/>
          <polyline points="1.5,4 10,11 18.5,4" fill="none" stroke="var(--brand-yellow)" stroke-width="1.6"/>
        </svg>
        <span>darren@glintservices.com.au</span>
      </li>
      <li class="contact-item">
        <svg class="contact-icon" viewBox="0 0 20 20" aria-hidden="true">
          <circle cx="10" cy="10" r="8" fill="none" stroke="var(--brand-yellow)" stroke-width="1.6"/>
          <ellipse cx="10" cy="10" rx="3.5" ry="8" fill="none" stroke="var(--brand-yellow)" stroke-width="1.4"/>
          <line x1="2" y1="10" x2="18" y2="10" stroke="var(--brand-yellow)" stroke-width="1.4"/>
        </svg>
        <span>pane-tidy-corner.com.au</span>
      </li>
    </ul>
  </section>
</main>
</body>
</html>
```